Business Card for Industrial Distributor

We need a business card design for an industrial distributor. We sell machine parts for the manufacturing and oil industry. We would like the cards to look clean and modern but with a touch of industry.

Our colors are blue/white.

Please feel free to visit our website www.krovelmint.com

Target Market(s)

mexican manufacturers in the automobile/aerospace industry

Industry/Entity Type

Industrial

Colors
ffffff
0555a3

```html
<!DOCTYPE html>
<html lang="en">
<head>
<meta charset="utf-8">
<title>Krovelmint Business Card</title>
<link href="https://fonts.googleapis.com/css2?family=PT+Sans:wght@400;700&display=swap" rel="stylesheet">
<style>
  :root {
    --brand-blue: #1356a3;
    --brand-navy: #2b2a7e;
    --deep-blue: #0d4585;
    --light-blue: #a9c0e6;
    --edge-blue: #1a7ac4;
    --white: #ffffff;
    --backdrop: #f2f2f2;
  }
  * { box-sizing: border-box; margin: 0; padding: 0; }
  html, body { width: 1200px; height: 1200px; overflow: hidden; }
  body {
    background: var(--backdrop);
    font-family: "PT Sans", sans-serif;
    position: relative;
  }
  .card {
    position: absolute;
    left: 264px;
    width: 672px;
    height: 388px;
    background: var(--brand-blue);
    overflow: hidden;
  }
  .card--front { top: 142px; }
  .card--back { top: 622px; }

  .card__header {
    position: absolute;
    left: 0; top: 0; right: 0;
    background: var(--white);
    display: flex;
    align-items: center;
  }
  .card--front .card__header { height: 155px; padding-left: 66px; gap: 18px; }
  .card--back .card__header { height: 84px; padding-left: 32px; gap: 10px; }

  .brand__mark {
    border-radius: 50%;
    background: var(--brand-navy);
    flex: none;
  }
  .card--front .brand__mark { width: 104px; height: 104px; }
  .card--back .brand__mark { width: 48px; height: 48px; }

  .brand__name {
    color: var(--brand-navy);
    font-weight: 700;
    line-height: 1;
  }
  .card--front .brand__name { font-size: 74px; }
  .card--back .brand__name { font-size: 36px; }

  .front__art {
    position: absolute;
    left: 0; right: 0;
    top: 200px; bottom: 0;
    background: linear-gradient(to right, var(--edge-blue), var(--light-blue) 25%, var(--white) 50%, var(--light-blue) 75%, var(--edge-blue));
    border-top: 8px solid var(--deep-blue);
  }
  .front__curve {
    position: absolute;
    left: 0; bottom: 0;
    width: 672px; height: 80px;
  }

  .back__gears {
    position: absolute;
    left: 384px; top: 20px;
    width: 288px; height: 64px;
    background: linear-gradient(to bottom, var(--white), var(--brand-blue));
    opacity: 0.55;
  }

  .contact {
    position: absolute;
    left: 134px; top: 104px;
    color: var(--white);
  }
  .contact__company { font-size: 34px; margin-bottom: 14px; }
  .contact__line { font-size: 24px; line-height: 37px; }
</style>
</head>
<body>
  <section class="card card--front">
    <header class="card__header">
      <span class="brand__mark"></span>
      <span class="brand__name">Krovelmint</span>
    </header>
    <div class="front__art" role="img" aria-label="Stylised wave band shading from blue edges to a white centre">
      <svg class="front__curve" viewBox="0 0 672 80" preserveAspectRatio="none" aria-hidden="true">
        <path d="M0 80 Q336 -20 672 80" fill="none" stroke="var(--deep-blue)" stroke-width="6"/>
      </svg>
    </div>
  </section>

  <section class="card card--back">
    <header class="card__header">
      <span class="brand__mark"></span>
      <span class="brand__name">Krovelmint</span>
    </header>
    <div class="back__gears" role="img" aria-label="Row of three gear silhouettes"></div>
    <div class="contact">
      <p class="contact__company">Krovelmint International Corp</p>
      <p class="contact__line">4120 Harlow Mill Rd.</p>
      <p class="contact__line">Corvale, TX 75120</p>
      <p class="contact__line">Tel: (555) 214 - 3307</p>
      <p class="contact__line">Fax: (555) 214 - 33071</p>
      <p class="contact__line">sales@krovelmint.com</p>
    </div>
  </section>
</body>
</html>
```